Stationery Design Project

I am a personal trainer in the fitness industry based in Miami. I have recently designed a logo for my company, now i need to market my name through selected stationery designs.
I need an email signature, invoice and a business card. I am looking for a design that is fresh and eye catching to my target audience.
Updates

Reason: Waiting for photo to be taken for business card.

Target Market(s)

25 to 65 years old - male and female - overweight, sedentary and athletic clientele - middle to wealthy economic class

Industry/Entity Type

Personal Trainer

Requirements
Must have
• Will attach Zip file with logo, template of invoice and personal information.
Will attach photo for business card in the next few days.
Nice to have
• Black backdrop logo image for banner of Invoice, with transparent images of my logo.
White backdrop logo image for Email signature, with font that works well with logo.

```html
<!DOCTYPE html>
<html lang="en">
<head>
<meta charset="utf-8">
<title>Corestride Fitness – Invoice</title>
<link href="https://fonts.googleapis.com/css2?family=Montserrat:wght@700&family=Questrial&display=swap" rel="stylesheet">
<style>
  :root {
    --paper: #ffffff;
    --ink: #1d1d1d;
    --ink-soft: #3a3a3a;
    --field: #eeefef;
    --rule: #ffffff;
    --brand: #2b2b2b;
  }
  * { margin: 0; padding: 0; box-sizing: border-box; }
  html, body { width: 848px; height: 1200px; overflow: hidden; background: var(--paper); }
  body { font-family: "Questrial", sans-serif; color: var(--ink); }
  .invoice { position: relative; width: 848px; height: 1200px; }

  .brand { position: absolute; left: 78px; top: 62px; width: 310px; text-align: center; }
  .brand-dot { width: 110px; height: 110px; border-radius: 50%; background: var(--brand); margin: 0 auto 22px; }
  .brand-name { font-size: 27px; letter-spacing: 1px; color: var(--brand); text-transform: uppercase; }

  .sender { position: absolute; left: 485px; top: 55px; font-size: 16px; line-height: 18.5px; color: var(--ink-soft); }
  .doc-title { position: absolute; left: 485px; top: 206px; font-family: "Montserrat", sans-serif; font-weight: 700; font-size: 23px; }

  .billing { position: absolute; left: 181px; top: 278px; width: 485px; display: grid; grid-template-rows: repeat(5, 22px); gap: 1px; background: var(--rule); }
  .billing div { background: var(--field); font-size: 14px; padding: 3px 6px; }

  .invoice-meta { position: absolute; left: 78px; top: 439px; width: 693px; height: 24px; background: var(--field); font-size: 14px; }
  .invoice-meta span { position: absolute; top: 4px; }
  .meta-number { left: 6px; }
  .meta-due { left: 351px; }

  .items { position: absolute; left: 78px; top: 494px; width: 693px; display: grid;
    grid-template-columns: 106px 344px 122px 121px; grid-auto-rows: 26px; gap: 1px; background: var(--rule); }
  .items div { background: var(--field); }
  .items .head { font-size: 14px; text-align: center; padding-top: 5px; color: var(--ink-soft); }

  .totals { position: absolute; left: 440px; top: 871px; width: 331px; display: grid; grid-template-columns: 210px 121px; grid-auto-rows: 26px; row-gap: 1px; column-gap: 1px; }
  .totals .label { font-family: "Montserrat", sans-serif; font-weight: 700; font-size: 12px; text-align: right; padding: 7px 10px 0 0; }
  .totals .value { background: var(--field); }

  .payable { position: absolute; left: 78px; top: 928px; font-size: 15px; }
  .thanks { position: absolute; left: 0; width: 848px; top: 1012px; text-align: center; font-family: "Montserrat", sans-serif; font-weight: 700; font-size: 16px; }
</style>
</head>
<body>
<main class="invoice">
  <div class="brand">
    <div class="brand-dot"></div>
    <div class="brand-name">Corestride Fitness</div>
  </div>

  <address class="sender" style="font-style:normal">
    Dara Quinn Personal Training<br>
    42 Bayview Terrace<br>
    Suite 810<br>
    Miami, FL 33199<br>
    H: 305 555 0147<br>
    C: 305 555 0192<br>
    E:&nbsp; dara@corestridefitness.com
  </address>

  <h1 class="doc-title">INVOICE</h1>

  <section class="billing">
    <div>Billing To:</div><div></div><div></div><div></div><div></div>
  </section>

  <section class="invoice-meta">
    <span class="meta-number">Invoice No:</span>
    <span class="meta-due">Payment Due:</span>
  </section>

  <section class="items">
    <div class="head">Quantity</div><div class="head">Description</div><div class="head">Unit Price</div><div class="head">Line Total</div>
    <div></div><div></div><div></div><div></div>
    <div></div><div></div><div></div><div></div>
    <div></div><div></div><div></div><div></div>
    <div></div><div></div><div></div><div></div>
    <div></div><div></div><div></div><div></div>
    <div></div><div></div><div></div><div></div>
    <div></div><div></div><div></div><div></div>
    <div></div><div></div><div></div><div></div>
    <div></div><div></div><div></div><div></div>
    <div></div><div></div><div></div><div></div>
    <div></div><div></div><div></div><div></div>
    <div></div><div></div><div></div><div></div>
    <div></div><div></div><div></div><div></div>
  </section>

  <section class="totals">
    <div class="label">SUBTOTAL</div><div class="value"></div>
    <div class="label">SALES TAX</div><div class="value"></div>
    <div class="label">TOTAL</div><div class="value"></div>
  </section>

  <p class="payable">Please make all checks payable to Dara Quinn.</p>
  <p class="thanks">THANK YOU FOR YOUR BUSINESS</p>
</main>
</body>
</html>
```